Silver Creek Plumbing Business card & letter head design

We need a new business card and letter head for our plumbing company called silver creek plumbing. attached is the companys logo. We provide domestic and commercial plumbing services in regional western Australia. We are after Something simple yet nice to look at and something that fits within the trade industry.

Target Market(s)

trade/building industry

Contact Information for Business Card

Darl Hensby
Manager
0461 238 574
enquiries@scplumbwork.net.au
ABN: 47 381 905 462
PCL: 5187

Domestic & Commercial Plumbing
Tip Truck & Excavator hire

Colors

Designer to choose colors to be used in the design.

```html
<!DOCTYPE html>
<html lang="en">
<head>
<meta charset="utf-8">
<title>Silver Creek Plumbing Letterhead</title>
<link href="https://fonts.googleapis.com/css2?family=Jost:wght@400;600&display=swap" rel="stylesheet">
<style>
  :root {
    --brand-blue: #1559b0;
    --band-dark: #0c4f9c;
    --band-mid: #1a6ab8;
    --band-edge: #b9bcc0;
    --faint-mark: #eef3f9;
    --paper: #ffffff;
    --ink-light: #ffffff;
  }
  html, body {
    margin: 0;
    padding: 0;
    overflow: hidden;
    background: var(--paper);
  }
  .letterhead {
    position: relative;
    width: 848px;
    height: 1200px;
    background: var(--paper);
    overflow: hidden;
    font-family: "Jost", sans-serif;
  }
  .brand-name {
    position: absolute;
    left: 60px;
    top: 58px;
    display: flex;
    align-items: center;
    gap: 10px;
    margin: 0;
    font-size: 24px;
    font-weight: 600;
    color: var(--brand-blue);
    letter-spacing: 0.2px;
    line-height: 1.1;
  }
  .brand-square {
    width: 18px;
    height: 18px;
    background: var(--brand-blue);
    flex: none;
  }
  .background-name {
    position: absolute;
    left: 0;
    right: 0;
    top: 520px;
    text-align: center;
    font-size: 78px;
    font-weight: 600;
    line-height: 1.05;
    color: var(--faint-mark);
    margin: 0;
  }
  .footer-band {
    position: absolute;
    left: 0;
    bottom: 0;
    width: 100%;
    height: 62px;
    background: linear-gradient(90deg, var(--band-dark) 0%, var(--band-mid) 50%, var(--band-dark) 100%);
    border-top: 5px solid var(--band-edge);
    box-sizing: border-box;
  }
  .footer-details {
    position: absolute;
    left: 79px;
    top: 15px;
    margin: 0;
    font-size: 20px;
    font-weight: 400;
    color: var(--ink-light);
    letter-spacing: 0.3px;
    white-space: nowrap;
  }
</style>
</head>
<body>
  <main class="letterhead">
    <h1 class="brand-name"><span class="brand-square"></span>Silver Creek Plumbing</h1>
    <p class="background-name" aria-hidden="true">Silver Creek<br>Plumbing</p>
    <footer class="footer-band">
      <p class="footer-details">Email: enquiries@scplumbwork.net.au, ABN: 47 381 905 462, PCL: 5187</p>
    </footer>
  </main>
</body>
</html>
```